stationary design

Marketing stationary. Nothing complicated please. My LOGO was designed here and I just want it attached to most of my stationary. I am not yet into Flyers and banners.
I have a consulting firm that is handling all other aspects of my business.
Thank you.

```html
<!DOCTYPE html>
<html lang="en">
<head>
<meta charset="utf-8">
<title>Brightfield Neighbors Home Care — Stationery Set</title>
<link rel="stylesheet" href="https://fonts.googleapis.com/css2?family=Montserrat:wght@300;700&family=Quicksand:wght@500;600&display=swap">
<style>
  :root{
    --green:#7da61c;
    --cyan:#6ccbd3;
    --navy:#14243a;
    --paper:#ffffff;
    --paper-soft:#f4f5f4;
    --ink:#3b4048;
    --muted:#6d737b;
    --backdrop:#e4e5e6;
  }
  *{box-sizing:border-box;margin:0;padding:0}
  html,body{width:1200px;height:786px;overflow:hidden}
  body{background:var(--backdrop);position:relative;font-family:"Quicksand",sans-serif;color:var(--ink)}
  .piece{position:absolute;background:var(--paper);box-shadow:0 2px 6px rgba(0,0,0,.12);overflow:hidden}
  .band{position:absolute;left:0;width:100%;background:linear-gradient(90deg,var(--green),var(--cyan))}
  .band--reverse{background:linear-gradient(90deg,var(--cyan),var(--green))}
  .brand{display:flex;align-items:center;gap:6px;font-family:"Montserrat",sans-serif;font-weight:700;color:var(--green);text-transform:uppercase;letter-spacing:.02em;line-height:1.15}
  .brand-dot{flex:none;border-radius:50%;background:var(--green)}

  /* letterhead */
  .letterhead{left:40px;top:36px;width:300px;height:424px}
  .letterhead .band--top{top:0;height:26px}
  .letterhead .masthead{position:absolute;top:26px;left:0;width:100%;height:110px;background:var(--paper-soft)}
  .letterhead .brand{position:absolute;left:22px;top:44px;font-size:10px;width:120px}
  .letterhead .brand-dot{width:14px;height:14px}
  .contact{position:absolute;left:168px;top:40px;font-size:6.2px;font-weight:600;line-height:1.55;color:var(--ink);font-style:normal}
  .contact .gap{margin-top:5px}
  .subject{position:absolute;left:32px;top:150px;font-family:"Montserrat",sans-serif;font-weight:300;font-size:10.5px;color:var(--ink)}
  .letter-body{position:absolute;left:32px;top:170px;width:236px;font-size:4.8px;line-height:1.6;color:var(--muted);text-align:justify}
  .letter-body p+p{margin-top:6px}
  .letterhead .band--bottom{bottom:0;height:42px}

  /* envelope front */
  .envelope{left:40px;top:490px;width:300px;height:150px}
  .envelope .brand{position:absolute;left:16px;top:24px;font-size:9px;width:110px}
  .envelope .brand-dot{width:12px;height:12px}
  .envelope .band--bottom{bottom:0;height:26px}
  .envelope .window{position:absolute;left:170px;top:56px;width:112px;height:50px;border-radius:4px;background:linear-gradient(160deg,#f2f3f4,#d6d9dc);border:1px solid #cfd3d6}
  .envelope .sender{position:absolute;left:10px;top:84px;font-size:4.6px;font-weight:600;line-height:1.7;color:var(--ink)}
  .envelope .sender span{display:inline-block;width:5px;height:5px;border-radius:50%;background:var(--green);margin-right:3px;vertical-align:middle}

  /* notebook cover */
  .notebook{left:380px;top:36px;width:210px;height:280px}
  .notebook .brand{position:absolute;left:18px;top:38px;font-size:9px;width:150px}
  .notebook .brand-dot{width:12px;height:12px}
  .notebook .band--bottom{bottom:34px;height:70px}

  /* disc sleeve */
  .sleeve{left:380px;top:346px;width:210px;height:190px}
  .sleeve .brand{position:absolute;left:14px;top:34px;font-size:9px;width:150px}
  .sleeve .brand-dot{width:12px;height:12px}
  .sleeve .band--bottom{bottom:28px;height:58px}

  /* tote bag face */
  .tote{left:630px;top:36px;width:280px;height:350px}
  .tote .band--mid{top:170px;height:100px}
  .tote .brand{position:absolute;right:18px;bottom:26px;font-size:10px;width:210px;justify-content:flex-end;text-align:right}
  .tote .brand-dot{width:14px;height:14px}

  /* header strip */
  .strip{left:630px;top:416px;width:530px;height:66px}
  .strip .brand{position:absolute;left:14px;top:26px;font-size:9px;white-space:nowrap}
  .strip .brand-dot{width:12px;height:12px}
  .strip .band--right{top:16px;left:auto;right:0;width:290px;height:50px}

  /* button badge */
  .badge{left:950px;top:36px;width:130px;height:130px;border-radius:50%}
  .badge .brand{position:absolute;left:18px;top:36px;font-size:8px;width:96px}
  .badge .brand-dot{width:10px;height:10px}
  .badge .band--bottom{bottom:10px;height:36px}

  /* mug wrap */
  .mug-wrap{left:950px;top:196px;width:210px;height:190px}
  .mug-wrap .brand{position:absolute;left:20px;top:34px;font-size:9px;width:170px}
  .mug-wrap .brand-dot{width:12px;height:12px}
  .mug-wrap .band--bottom{bottom:18px;height:56px}

  /* envelope back */
  .envelope-back{left:380px;top:566px;width:300px;height:180px}
  .envelope-back .flap{position:absolute;left:0;top:0;width:100%;height:80px;display:block}
</style>
</head>
<body>

<section class="piece letterhead" aria-label="Letterhead">
  <div class="band band--top band--reverse" role="img" aria-label="Brand colour band"></div>
  <header class="masthead">
    <div class="brand"><span class="brand-dot"></span>Brightfield Neighbors Home Care</div>
    <address class="contact">
      Four Harbor Court<br>Suite 310, Millbrook, NJ
      <div class="gap">hello@brightfieldcare.com</div>
      <div class="gap">555-201-0147</div>
    </address>
  </header>
  <h1 class="subject">SUBJECT HEADLINE HERE</h1>
  <div class="letter-body">
    <p>Lorem ipsum dolor sit amet, consectetur adipiscing elit. Fusce dignissim pretium consectetur. Curabitur tempor posuere massa in varius. Pellentesque viverra nibh eu vehicula mattis. Nullam porta facilisis justo, a feugiat dolor sodales sed. Vestibulum neque nisi, elementum tincidunt metus sit amet, egestas bibendum enim. Aenean a blandit elit, vel rutrum mi. Nunc dapibus turpis sed massa aliquet tincidunt.</p>
    <p>Pellentesque id neque ligula. Nullam posuere, ligula a mattis posuere, lacus nisl adipiscing nunc, eu congue justo est ut diam. Nam quam nibh, dignissim non consequat in, semper eget purus. Nulla arcu sapien, viverra vitae metus tempor, congue ornare diam.</p>
    <p>Pellentesque vel nibh tempus, ullamcorper tortor sed, bibendum augue. Phasellus sollicitudin justo et quam aliquam sollicitudin. Sed eget nibh mollis, mattis sem et, viverra nulla.</p>
  </div>
  <div class="band band--bottom" role="img" aria-label="Brand colour band"></div>
</section>

<section class="piece envelope" aria-label="Envelope front">
  <div class="brand"><span class="brand-dot"></span>Brightfield Neighbors Home Care</div>
  <div class="window"></div>
  <div class="sender">
    <div><span></span>Four Harbor Court, Suite 310, Millbrook, NJ</div>
    <div><span></span>hello@brightfieldcare.com</div>
    <div><span></span>555-201-0147</div>
  </div>
  <div class="band band--bottom" role="img" aria-label="Brand colour band"></div>
</section>

<section class="piece notebook" aria-label="Notebook cover">
  <div class="brand"><span class="brand-dot"></span>Brightfield Neighbors Home Care</div>
  <div class="band band--bottom" role="img" aria-label="Brand colour band"></div>
</section>

<section class="piece sleeve" aria-label="Disc sleeve">
  <div class="brand"><span class="brand-dot"></span>Brightfield Neighbors Home Care</div>
  <div class="band band--bottom" role="img" aria-label="Brand colour band"></div>
</section>

<section class="piece tote" aria-label="Tote bag face">
  <div class="band band--mid" role="img" aria-label="Brand colour band"></div>
  <div class="brand"><span class="brand-dot"></span>Brightfield Neighbors Home Care</div>
</section>

<section class="piece strip" aria-label="Header strip">
  <div class="brand"><span class="brand-dot"></span>Brightfield Neighbors Home Care</div>
  <div class="band band--right" role="img" aria-label="Brand colour band"></div>
</section>

<section class="piece badge" aria-label="Button badge">
  <div class="brand"><span class="brand-dot"></span>Brightfield Neighbors</div>
  <div class="band band--bottom" role="img" aria-label="Brand colour band"></div>
</section>

<section class="piece mug-wrap" aria-label="Mug wrap">
  <div class="brand"><span class="brand-dot"></span>Brightfield Neighbors Home Care</div>
  <div class="band band--bottom" role="img" aria-label="Brand colour band"></div>
</section>

<section class="piece envelope-back" aria-label="Envelope back">
  <svg class="flap" viewBox="0 0 300 80" preserveAspectRatio="none">
    <path d="M0,0 H300 V20 L268,68 Q262,78 250,78 H50 Q38,78 32,68 L0,20 Z" fill="var(--navy)"/>
  </svg>
</section>

</body>
</html>
```